website design Investment Fund

I am looking for a custom website that will work on desktop computer, tablet device and a cellular device. I have attached the booklet so you can get an idea of the look we are going for. Would like to use the website eventually for crowdfunding. We like the ski racer and mountain climbing designs.

Target Market(s)

Financial Services

Industry/Entity Type

Financial Service

Coding

Coded - Design and coding required

Number of Pages Required

5+ page

Font styles to use
Sans Serif

Requirements
Must have
• Must be viewable on a cell phone and tablet and desktop
Nice to have
• Contact us form

```html
<!DOCTYPE html>
<html lang="en">
<head>
<meta charset="utf-8">
<title>Alpine Ridge Capital</title>
<meta name="viewport" content="width=1200">
<link href="https://fonts.googleapis.com/css2?family=Source+Sans+3:wght@400;600;700&display=swap" rel="stylesheet">
<style>
:root{
  --red:#e1232b;
  --blue:#1d4fa3;
  --navy:#173a7a;
  --ink:#2b2b2b;
  --muted:#666;
  --dark:#1c1c1c;
  --card:#161616;
  --light:#f4f4f4;
  --white:#fff;
}
*{box-sizing:border-box;margin:0;padding:0}
html,body{width:1200px;height:5157px;overflow:hidden}
body{font-family:"Source Sans 3",Arial,sans-serif;color:var(--ink);background:var(--white);position:relative}
.abs{position:absolute}
.stripes{position:absolute;left:0;width:1200px}

/* header */
.site-header{top:0;left:0;width:1200px;height:106px;background:var(--white);z-index:5}
.brand{left:90px;top:30px;display:flex;align-items:center;gap:10px}
.brand-mark{width:16px;height:16px;background:var(--red)}
.brand-name{font-size:17px;font-weight:700;color:var(--navy);letter-spacing:.5px}
.main-nav{right:90px;top:27px;display:flex;gap:24px;align-items:center;font-size:12px}
.main-nav a{color:var(--ink);text-decoration:none;padding:6px 10px}
.main-nav a.current{border:2px solid var(--red);border-radius:16px;color:var(--red);padding:5px 24px}

/* hero */
.hero{top:106px;left:0;width:1200px;height:540px;background:linear-gradient(180deg,#6c7c90 0%,#c9d2da 35%,#eef1f4 70%,#dfe4e9 100%)}
.hero-title{top:180px;left:0;width:1200px;text-align:center;font-weight:700;font-size:52px;line-height:56px;letter-spacing:.5px}
.hero-title .l1{color:var(--red);display:block}
.hero-title .l2{color:var(--blue);display:block}
.hero-arrow{top:222px;width:30px;height:30px;border:2px solid #fff;border-radius:50%}
.hero-arrow svg{display:block;margin:6px auto}
.hero-dots{top:318px;left:574px;display:flex;gap:8px}
.hero-dots i{width:10px;height:10px;border-radius:50%;background:#fff;display:block}
.hero-dots i.on{background:#333;border:2px solid #fff}

/* about */
.about{top:646px;left:0;width:1200px;height:520px;background:linear-gradient(90deg,#fff 40%,#e9e9e9 100%)}
.about-art{left:94px;top:32px}
.about-text{left:522px;top:78px;width:570px}
.sec-title{font-size:38px;font-weight:600;line-height:40px;color:var(--ink)}
.sec-sub{font-size:30px;font-weight:400;line-height:34px;color:var(--ink);letter-spacing:1px}
.about-text p{font-size:11px;line-height:19px;color:var(--muted);margin-top:14px}
.btn{display:inline-block;background:var(--red);color:#fff;font-weight:700;border-radius:20px;text-decoration:none}
.about-text .btn{font-size:11px;padding:10px 28px;margin-top:16px}

/* strategy */
.strategy{top:1130px;left:0;width:1200px;height:600px;background:linear-gradient(180deg,#3a3a3a,#262626 60%,#3b3b3b)}
.strategy-card{top:100px;width:497px;height:330px;background:var(--card);color:#fff;padding:36px 32px}
.strategy-card h3{font-size:22px;font-weight:700;line-height:29px;margin-top:18px;letter-spacing:.5px}
.strategy-card p{font-size:11px;line-height:19px;color:#ddd;margin-top:8px}

/* office */
.office-head{top:1790px;left:0;width:1200px;text-align:center}
.office-head .sec-title{font-size:38px}
.photo{background:#999}

/* investors */
.investors{top:2510px;left:0;width:1200px;height:990px;background:linear-gradient(180deg,#303030,#1e1e1e 50%,#3a3a3a)}
.investors h2{top:155px;left:0;width:1200px;text-align:center;color:#fff;font-size:38px;font-weight:600}
.offer{top:215px;width:494px;height:600px;background:#fff;text-align:center;overflow:hidden}
.offer-img{height:265px}
.offer h4{font-size:25px;font-weight:600;line-height:31px;color:#333;margin-top:30px}
.offer .series{display:inline-block;background:var(--red);color:#fff;font-weight:700;font-size:17px;padding:9px 30px;margin-top:12px;min-width:288px}
.offer h5{font-size:24px;font-weight:600;color:#333;margin-top:18px}
.offer .rate{font-size:15px;color:#555;margin-top:4px}
.offer .term{font-size:15px;color:#555;margin-top:14px}
.offer svg{position:absolute;left:0;bottom:0}

/* team */
.team-head{top:3555px;left:0;width:1200px;text-align:center}
.team-card{top:3650px;left:94px;width:990px;height:368px;background:#fff;box-shadow:0 0 14px rgba(0,0,0,.12)}
.team-card .name{position:absolute;left:52px;top:62px;color:var(--red);font-size:15px;font-weight:700}
.team-card .role{position:absolute;left:52px;top:84px;color:var(--blue);font-size:11px;display:flex;align-items:center;gap:6px}
.team-card .role::before{content:"";width:20px;height:1px;background:var(--blue)}
.team-card .bio{position:absolute;left:52px;top:112px;width:710px;font-size:11px;line-height:20px;color:#555}
.team-card .rule{position:absolute;left:52px;top:200px;width:600px;height:1px;background:#ddd}
.thumb{position:absolute;top:225px;width:72px;height:72px;border-radius:50%;background:radial-gradient(circle,#c9b9a8,#7d7368)}
.thumb.active{border:3px solid var(--red)}
.portrait{position:absolute;left:802px;top:104px;width:134px;height:152px;border:3px solid #ddd;background:linear-gradient(180deg,#9aa6b6,#5b6677)}
.pager{left:1134px;width:22px;height:22px;border:2px solid var(--blue);border-radius:50%}
.pager svg{display:block;margin:3px auto}

/* contact */
.contact{top:4270px;left:0;width:1200px;height:370px;background:linear-gradient(180deg,#111,#1d1d1d)}
.contact h3{color:#fff;font-size:26px;font-weight:700;position:absolute;top:30px}
.field{position:absolute;background:#2d2d2d;color:#aaa;font-size:10px;padding:10px 14px}
.contact .submit{position:absolute;left:94px;top:255px;font-size:12px;padding:10px 32px}
.info{position:absolute;left:798px;color:#fff;font-size:10px;line-height:16px;display:flex;gap:8px}
.info b{font-size:12px;display:block}
.social{position:absolute;left:798px;top:228px;display:flex;gap:12px}
.social i{width:30px;height:30px;border-radius:50%;background:var(--blue);border:2px solid #fff;display:block}
.social i.pink{background:#c13584}

/* footer */
.footer-main{top:4640px;left:0;width:1200px;height:244px;background:var(--light)}
.fcol{position:absolute;top:62px}
.fcol h4{color:var(--blue);font-size:17px;font-weight:600;margin-bottom:18px}
.fcol p{font-size:10px;line-height:19px;color:#777;width:250px}
.fdiv{position:absolute;top:100px;width:1px;height:100px;background:#ccc}
.links{display:grid;grid-template-columns:106px 100px;row-gap:12px;font-size:11px;color:#555}
.links span{display:flex;align-items:center;gap:6px}
.links span::before{content:"";width:9px;height:9px;border-radius:50%;background:var(--red)}
.email{width:266px;height:34px;border:1px solid #ccc;border-radius:18px;background:#fff;font-size:10px;color:#999;padding:10px 22px}
.fcol .btn{font-size:12px;padding:10px 26px;margin-top:10px}
.phone-band{top:4884px;left:0;width:1200px;height:84px;background:var(--red);display:flex;padding-left:94px}
.phone-item{width:255px;display:flex;align-items:center;gap:10px;color:#fff;font-size:11px;font-weight:700;line-height:20px;padding-left:44px;border-right:1px solid rgba(255,255,255,.5);height:56px;margin-top:14px}
.phone-item:last-child{border-right:none}
.bottom{top:4968px;left:0;width:1200px;height:189px;background:#121212;text-align:center}
.bottom .brand-name{color:#fff;font-size:15px;display:inline-flex;align-items:center;gap:8px;margin-top:72px}
.bottom .brand-name::before{content:"";width:12px;height:12px;background:var(--red)}
.bottom p{color:#ccc;font-size:10px;margin-top:18px}
.bottom p em{color:var(--red);font-style:normal}
</style>
</head>
<body>

<header class="abs site-header">
  <div class="abs brand"><span class="brand-mark"></span><span class="brand-name">ALPINE RIDGE CAPITAL</span></div>
  <nav class="abs main-nav">
    <a class="current">Home</a><a>About us</a><a>Services</a><a>Our Team Our</a><a>Scottsdale</a><a>Contact</a>
  </nav>
</header>

<section class="abs hero" role="img" aria-label="Skier carving through deep powder snow on a mountain slope">
  <h1 class="abs hero-title"><span class="l1">YOUR ELITE BOUTIQUE LENDER</span><span class="l2">WHERE CREATIVITY COUNTS</span></h1>
  <div class="abs hero-arrow" style="left:22px"><svg width="14" height="14" viewBox="0 0 14 14"><path d="M9 2 4 7l5 5M4 7h9" stroke="#fff" stroke-width="2" fill="none"/></svg></div>
  <div class="abs hero-arrow" style="right:22px"><svg width="14" height="14" viewBox="0 0 14 14"><path d="M5 2l5 5-5 5M10 7H1" stroke="#fff" stroke-width="2" fill="none"/></svg></div>
  <div class="abs hero-dots"><i></i><i class="on"></i><i></i></div>
</section>
<svg class="stripes" style="top:480px;z-index:2" width="1200" height="180" viewBox="0 0 1200 180">
  <polygon points="0,166 1200,10 1200,180 0,180" fill="#fff"/>
  <polygon points="0,156 600,80 600,86 0,166" fill="#1d4fa3"/>
  <polygon points="600,80 1200,4 1200,14 600,88" fill="#e1232b"/>
</svg>

<section class="abs about" style="z-index:1">
  <svg class="abs about-art" width="392" height="370" viewBox="0 0 392 370" role="img" aria-label="Climber standing on a rocky summit against a blue sky, framed in a triangle">
    <defs><linearGradient id="sky" x1="0" y1="0" x2="0" y2="1"><stop offset="0" stop-color="#4a6a90"/><stop offset=".6" stop-color="#7c8ba0"/><stop offset="1" stop-color="#3a3a42"/></linearGradient></defs>
    <polygon points="192,0 392,366 0,366" fill="url(#sky)"/>
  </svg>
  <div class="abs about-text">
    <h2 class="sec-title">ABOUT</h2>
    <div class="sec-sub">The Company</div>
    <p>Ridgeline Funding &amp; Investment, Inc. is a privately held mortgage lender, asset management and advisory firm headquartered in Scottsdale, Arizona which specializes in fast financing for debt, equity, mezzanine and land bank on real estate projects in the $100,000 to $50,000,000 range. As a highly reputable, successful and growth-focused company with decades of experience across the entire spectrum of real estate financing through Arizona,the Southwest United States and Mexico.</p>
    <a class="btn">Know More About Us</a>
  </div>
</section>

<section class="abs strategy" role="img" aria-label="Dark mountain landscape backdrop">
  <div class="abs strategy-card" style="left:94px">
    <svg width="84" height="84" viewBox="0 0 84 84" fill="none" stroke="#fff" stroke-width="2.5"><path d="M20 50a14 14 0 0 1 2-27 20 20 0 0 1 38 2 12 12 0 0 1 4 24"/><circle cx="42" cy="46" r="14"/><path d="M46 40h-6a3 3 0 0 0 0 6h4a3 3 0 0 1 0 6h-6M42 36v4M42 52v4"/><circle cx="16" cy="66" r="8"/><circle cx="66" cy="66" r="8"/></svg>
    <h3>THE BOUTIQUE FUND<br>INVESTORS ARE LOOKING FOR</h3>
    <p>As an ELITE BOUTIQUE, full-service, and highly selective firm, we only present our investors deals with highly qualified borrowers and properties with loan to value ratios (LTV) not to exceed 65%-70%. Simply put, we only fund deals with enough equity to allow for a Real Estate market change. All loans are short term so we can easily monitor changes in valuation and market conditions.</p>
  </div>
  <div class="abs strategy-card" style="left:605px">
    <svg width="84" height="84" viewBox="0 0 84 84" fill="none" stroke="#fff" stroke-width="2.5"><path d="M8 58h14l14 6h22l16-10M22 74h-14"/><path d="M34 48V24M46 48V14M58 48V26"/><path d="M28 30l6-6 6 6M40 20l6-6 6 6M52 32l6-6 6 6"/></svg>
    <h3>INVESTMENT<br>STRATEGY:</h3>
    <p>The Fund Managers have decades of experience in private money lending as well as real estate investment, property and asset management, construction, and development. In order to produce the desired investor yields, the Fund Managers will utilize their extensive relationships in the marketplace to make a diversified series of investments in secured loans, equity joint ventures, and select value-add real estate investments.</p>
  </div>
</section>
<svg class="stripes" style="top:1100px" width="1200" height="80" viewBox="0 0 1200 80">
  <polygon points="0,80 0,66 1200,0 1200,80" fill="#3a3a3a"/>
  <polygon points="0,62 1200,0 1200,8 0,70" fill="#e1232b"/>
</svg>
<svg class="stripes" style="top:1620px" width="1200" height="120" viewBox="0 0 1200 120">
  <polygon points="0,110 1200,24 1200,120 0,120" fill="#fff"/>
  <polygon points="0,104 700,52 700,58 0,112" fill="#1d4fa3"/>
  <polygon points="700,52 1200,16 1200,26 700,60" fill="#e1232b"/>
</svg>

<section class="abs office-head">
  <h2 class="sec-title">OUR SCOTTSDALE, ARIZONA</h2>
  <div class="sec-sub">Corporate Office</div>
</section>
<div class="abs photo" style="left:94px;top:1885px;width:308px;height:332px;background:linear-gradient(180deg,#4d6e8c,#8aa0b0 60%,#5d6b4c)" role="img" aria-label="Glass office tower exterior"></div>
<div class="abs photo" style="left:94px;top:2224px;width:308px;height:226px;background:linear-gradient(180deg,#e9e6e1,#cfc8bf)" role="img" aria-label="Minimal conference room with dining table"></div>
<div class="abs photo" style="left:410px;top:1885px;width:380px;height:280px;background:linear-gradient(180deg,#d8dbdf,#6f747a)" role="img" aria-label="Team meeting around laptops"></div>
<div class="abs photo" style="left:410px;top:2172px;width:380px;height:278px;background:linear-gradient(180deg,#e6e9ec,#8c939b)" role="img" aria-label="Looking up at high-rise towers"></div>
<div class="abs photo" style="left:797px;top:1885px;width:308px;height:227px;background:linear-gradient(180deg,#c9c4a0,#4a4640)" role="img" aria-label="Open-plan office lounge with yellow wall"></div>
<div class="abs photo" style="left:797px;top:2119px;width:308px;height:331px;background:linear-gradient(160deg,#1e6fd6,#7fb4e0 60%,#3d6a8e)" role="img" aria-label="Blue glass building facade against sky"></div>

<section class="abs investors" role="img" aria-label="Dark snowy mountain backdrop">
  <h2 class="abs">ACCREDITED INVESTORS ONLY</h2>
  <div class="abs offer" style="left:94px">
    <div class="offer-img" style="background:linear-gradient(180deg,#c4533f,#7e5a48 60%,#cfc7bd)" role="img" aria-label="Hands counting stacked coins"></div>
    <h4>MINIMUM INVESTMENT<br>REQUIREMENTS</h4>
    <div class="series">SERIES A $50,000-$249,999</div>
    <h5>RATE OF RETURN</h5>
    <div class="rate">SERIES A 7% PER ANNUM</div>
    <div class="term">Term 24 months</div>
    <svg width="494" height="54" viewBox="0 0 494 54"><path d="M0 20q20-16 41 0t41 0 41 0 41 0 41 0 41 0 41 0 41 0 41 0 41 0 41 0 41 0 42 0V54H0z" fill="#1d4fa3"/></svg>
  </div>
  <div class="abs offer" style="left:612px">
    <div class="offer-img" style="background:linear-gradient(180deg,#d3d5d8,#8f969f 60%,#5f6f84)" role="img" aria-label="Business handshake over a laptop"></div>
    <h4>MINIMUM INVESTMENT<br>REQUIREMENTS</h4>
    <div class="series">SERIES B $250,000.00</div>
    <h5>RATE OF RETURN</h5>
    <div class="rate">SERIES A 8% PER ANNUM</div>
    <div class="term">Term 24 months</div>
    <svg width="494" height="54" viewBox="0 0 494 54"><path d="M0 20q20-16 41 0t41 0 41 0 41 0 41 0 41 0 41 0 41 0 41 0 41 0 41 0 41 0 42 0V54H0z" fill="#1d4fa3"/></svg>
  </div>
</section>
<svg class="stripes" style="top:2500px" width="1200" height="110" viewBox="0 0 1200 110">
  <polygon points="0,0 1200,0 1200,14 0,100" fill="#fff"/>
  <polygon points="0,100 600,56 600,64 0,110" fill="#e1232b"/>
  <polygon points="600,56 1200,12 1200,22 600,64" fill="#1d4fa3"/>
</svg>
<svg class="stripes" style="top:3400px" width="1200" height="110" viewBox="0 0 1200 110">
  <polygon points="0,110 0,96 1200,20 1200,110" fill="#fff"/>
  <polygon points="0,88 1200,14 1200,22 0,98" fill="#1d4fa3"/>
</svg>

<section class="abs team-head">
  <h2 class="sec-title">OUR TEAM</h2>
  <div class="sec-sub">Founding Members And Fund Managers</div>
</section>
<article class="abs team-card">
  <div class="name">DANIEL R. HALE</div>
  <div class="role">Founder &amp; Fund Manager</div>
  <p class="bio">Daniel is a real estate development and finance entrepreneur and executive with over 37 years of entrepreneur experience. As the Founder, Chairman and CEO of Ridgeline Funding and Investments, Inc, a privately held mortgage lender and advisory firm headquartered in Scottsdale Arizona, he has raised and funded through his companies over 1 billion dollars in debt, equity, mezzanine and joint ventures with a wide range of asset classes.</p>
  <div class="rule"></div>
  <svg class="abs" style="left:81px;top:194px" width="12" height="8" viewBox="0 0 12 8"><path d="M0 8 6 0l6 8z" fill="#e1232b"/></svg>
  <div class="thumb active" style="left:50px" role="img" aria-label="Portrait of Daniel R. Hale"></div>
  <div class="thumb" style="left:142px;background:radial-gradient(circle,#e0cfa8,#9d8b6a)" role="img" aria-label="Portrait of Carla Vescio"></div>
  <div class="thumb" style="left:233px;background:radial-gradient(circle,#c9c9c9,#6d6d6d)" role="img" aria-label="Portrait of Peter Lanz"></div>
  <div class="thumb" style="left:324px;background:radial-gradient(circle,#d2d2d2,#6a6a6a)" role="img" aria-label="Portrait of Sam Okafor"></div>
  <div class="portrait" role="img" aria-label="Portrait of Daniel R. Hale"></div>
</article>
<div class="abs pager" style="top:3810px"><svg width="12" height="12" viewBox="0 0 12 12"><path d="M6 10V2M2 6l4-4 4 4" stroke="#1d4fa3" stroke-width="1.6" fill="none"/></svg></div>
<div class="abs pager" style="top:3845px"><svg width="12" height="12" viewBox="0 0 12 12"><path d="M6 2v8M2 6l4 4 4-4" stroke="#1d4fa3" stroke-width="1.6" fill="none"/></svg></div>

<section class="abs contact">
  <h3 style="left:96px">GET IN TOUCH</h3>
  <div class="field" style="left:94px;top:82px;width:315px;height:34px">Name :</div>
  <div class="field" style="left:415px;top:82px;width:313px;height:34px">Email :</div>
  <div class="field" style="left:94px;top:124px;width:634px;height:34px">Mobile :</div>
  <div class="field" style="left:94px;top:166px;width:634px;height:76px">Message :</div>
  <a class="btn submit">Submit Now</a>
  <h3 style="left:795px">CONTACT INFORMATION</h3>
  <div class="info" style="top:88px">
    <svg width="18" height="18" viewBox="0 0 18 18" fill="none" stroke="#fff" stroke-width="1.4"><circle cx="9" cy="9" r="8"/><path d="M9 14s-4-4-4-6.5a4 4 0 0 1 8 0C13 10 9 14 9 14z"/><circle cx="9" cy="7.5" r="1.4"/></svg>
    <div><b>Address :</b>2100 N. Summit Ridge Blvd Suite 9<br>Scottsdale, AZ 85250</div>
  </div>
  <div class="info" style="top:158px">
    <svg width="18" height="18" viewBox="0 0 18 18" fill="none" stroke="#fff" stroke-width="1.4"><circle cx="9" cy="9" r="8"/><path d="M6 5l2 2-1 1.5a6 6 0 0 0 2.5 2.5L11 10l2 2-1.5 1.5C8 13 5 10 4.5 6.5z"/></svg>
    <div><b>Call Us On :</b>DANIEL R. HALE : 480-555-0142</div>
  </div>
  <div class="social"><i role="img" aria-label="Social profile"></i><i role="img" aria-label="Social profile"></i><i role="img" aria-label="Social profile"></i><i class="pink" role="img" aria-label="Social profile"></i></div>
</section>
<svg class="stripes" style="top:4120px" width="1200" height="160" viewBox="0 0 1200 160">
  <polygon points="0,150 1200,20 1200,160 0,160" fill="#111"/>
  <polygon points="0,134 1200,8 1200,18 0,144" fill="#e1232b"/>
</svg>

<footer>
  <section class="abs footer-main">
    <div class="fcol" style="left:120px"><h4>About Us</h4><p>Ridgeline Funding &amp; Investment, Inc. is a privately held mortgage lender, asset management and advisory firm headquartered in Scottsdale, Arizona which specializes in fast financing for debt</p></div>
    <div class="fdiv" style="left:437px"></div>
    <div class="fcol" style="left:500px"><h4>Usefull Links</h4>
      <div class="links"><span>Home</span><span>Our Team</span><span>About us</span><span>Our Scottsdale</span><span>Services</span><span>Contact</span></div>
    </div>
    <div class="fdiv" style="left:768px"></div>
    <div class="fcol" style="left:826px"><h4>Subscribe Newsletter</h4><div class="email">Enter your Email</div><a class="btn">Subscribe Now</a></div>
  </section>
  <section class="abs phone-band">
    <div class="phone-item"><svg width="22" height="22" viewBox="0 0 22 22" fill="none" stroke="#fff" stroke-width="1.6"><path d="M5 3l4 4-2 2.5a9 9 0 0 0 5.5 5.5L15 13l4 4-2.5 2.5C10 19 3 12 2.5 5.5z"/><path d="M13 3a6 6 0 0 1 6 6M13 6.5a2.5 2.5 0 0 1 2.5 2.5"/></svg><div>DANIEL R. HALE<br>480-555-0142</div></div>
    <div class="phone-item"><svg width="22" height="22" viewBox="0 0 22 22" fill="none" stroke="#fff" stroke-width="1.6"><path d="M5 3l4 4-2 2.5a9 9 0 0 0 5.5 5.5L15 13l4 4-2.5 2.5C10 19 3 12 2.5 5.5z"/><path d="M13 3a6 6 0 0 1 6 6M13 6.5a2.5 2.5 0 0 1 2.5 2.5"/></svg><div>PETER LANZ<br>480-555-0187</div></div>
    <div class="phone-item"><svg width="22" height="22" viewBox="0 0 22 22" fill="none" stroke="#fff" stroke-width="1.6"><path d="M5 3l4 4-2 2.5a9 9 0 0 0 5.5 5.5L15 13l4 4-2.5 2.5C10 19 3 12 2.5 5.5z"/><path d="M13 3a6 6 0 0 1 6 6M13 6.5a2.5 2.5 0 0 1 2.5 2.5"/></svg><div>CARLA VESCIO<br>602-555-0163</div></div>
    <div class="phone-item"><svg width="22" height="22" viewBox="0 0 22 22" fill="none" stroke="#fff" stroke-width="1.6"><path d="M5 3l4 4-2 2.5a9 9 0 0 0 5.5 5.5L15 13l4 4-2.5 2.5C10 19 3 12 2.5 5.5z"/><path d="M13 3a6 6 0 0 1 6 6M13 6.5a2.5 2.5 0 0 1 2.5 2.5"/></svg><div>SAM OKAFOR<br>602-555-0119</div></div>
  </section>
  <section class="abs bottom">
    <div class="brand-name">ALPINE RIDGE CAPITAL</div>
    <p>Copyrights © 2019 <em>ALPINE RIDGE CAPITAL</em>. All Rights Reserved.</p>
  </section>
</footer>

</body>
</html>
```